Create an awesome website for a medical clinic

This is a new website for a doctor's office. The site should be clean and modern, easy to navigate.

This is a wellness clinic, we want to help our clients have a healthy, active lifestyle. It should be friendly and inviting, and easy for them to call or schedule an appointment.

The site should be responsive and designed using the attached Bootstrap 3 PSD.

We will provide stock photos, until then please use stock photos from:

photoharvestbin.net or
lumapicturevault.net (preferred)

Some example sites of clean and modern designs that we like:

https://tarnelspine.example/
http://walkpastjoints.example/
http://feelingbrisker.example/

Also attached is a temporary logo you can use.
Updates

Reason: Thank you everyone for your great designs - we need a little more time so I'm extending the project.

Need extra days to review

Also, the colors in the new logo I just linked to are the final colors of the logo, so feel free to use any complimentary colors to it.

Hi everyone, The boss wants to change the layout of the site a little bit - here's the revised layout: https://www.filecrate.example/s/q8vn31kd2pxe74rt/memo%2011_29_2017.pdf?dl=0 And the graphic assets you can use are here: https://www.filecrate.example/s/q8vn31kd2pxe74rt/memo%2011_29_2017.pdf?dl=0 Feel free to change the background color of the "topbar", and change the icons of the "why people trust us" if you want, these are just temporary placeholders. Thanks for your patience and hard work!

Target Market(s)

People seeking medical treatment (wellness clinic)

Industry/Entity Type

Doctor

Number of Pages Required

1 page

Font styles to use
Sans Serif

Colors
0592cd
33a6d7
abd037
9bcb3c

Requirements
Must have
• The home page should have: a strong hero image/slideshow, clinic phone number should be prominent and at the top of the page (in the nav), a "what to expect" section (this is like a FAQs section - see attachment), and a strong call to action (a button to call or schedule an appointment).
• The what to expect section is useful so that prospective clients can determine if we're a good fit for them or not. It's a basic, first-step pre-qualification block of information.
• Social media icons which links to our social media profiles should be included.
Nice to have
• - Link to 3 most recent blog entries
• - Testimonials
• - How a multilevel nav menu looks.

```html
<!DOCTYPE html>
<html lang="en">
<head>
<meta charset="utf-8">
<title>Fernvale Medical Clinic</title>
<link href="https://fonts.googleapis.com/css2?family=Roboto:wght@400;500;700&display=swap" rel="stylesheet">
<style>
:root{
  --blue-deep:#0592cd;
  --blue-soft:#33a6d7;
  --green:#9bcb3c;
  --green-bright:#abd037;
  --ink:#111;
  --footer:#1b1e21;
  --paper:#e9e9e9;
  --white:#fff;
}
*{margin:0;padding:0;box-sizing:border-box}
html,body{width:1200px;height:2362px;overflow:hidden}
body{font-family:'Roboto',sans-serif;color:var(--ink);background:var(--white);position:relative}
.abs{position:absolute}

/* top bar */
.topbar{position:absolute;top:0;left:0;width:1200px;height:109px;background:var(--white)}
.phone-badge{left:187px;top:35px;width:38px;height:38px;background:var(--green);border-radius:3px;display:flex;align-items:center;justify-content:center}
.phone-line{left:238px;top:47px;font-size:11.5px;font-weight:500}
.brand{left:500px;top:36px;width:200px;text-align:center;color:var(--green);font-weight:700;font-size:24px;line-height:24px;letter-spacing:.3px}
.brand small{display:block;color:var(--green);font-size:9.5px;font-weight:700;line-height:14px;letter-spacing:.8px}
.btn-book{left:833px;top:35px;width:177px;height:39px;background:var(--green);color:var(--white);font-size:11px;font-weight:700;display:flex;align-items:center;justify-content:center}

/* nav */
.main-nav{left:187px;top:109px;width:823px;height:34px;background:var(--blue-deep);z-index:3}
.main-nav a{position:absolute;top:0;line-height:34px;color:var(--white);font-size:14px;font-weight:500;text-decoration:none;transform:translateX(-50%);white-space:nowrap}
.main-nav a.active{color:var(--green-bright)}

/* hero */
.hero{left:0;top:143px;width:1200px;height:503px;background:linear-gradient(90deg,#f4f5f6 0%,#e8ebee 45%,#d9dde1 100%)}
.hero-photo{right:0;top:0;width:620px;height:503px;background:radial-gradient(ellipse at 55% 45%,#d8c0ae 0%,#cfd4d9 45%,rgba(225,229,233,0) 75%)}
.hero-title{left:86px;top:308px;font-size:19px;font-weight:400;letter-spacing:.3px}
.hero-text{left:87px;top:346px;font-size:13.5px;line-height:24px;white-space:nowrap}
.hero-btn{left:87px;top:435px;width:176px;height:36px;border-radius:18px;background:var(--blue-deep);color:var(--white);font-size:11px;font-weight:700;display:flex;align-items:center;justify-content:center}
.dots{display:flex;gap:6px}
.dots span{width:9px;height:9px;border-radius:50%;background:#b8d77a}
.dots span.on{background:var(--green)}

/* feature cards */
.card{top:587px;width:201px;height:224px;color:var(--white);text-align:center;border-bottom:4px solid #0a3c5a;z-index:2}
.card.deep{background:var(--blue-deep)}
.card.soft{background:var(--blue-soft)}
.card-icon{position:absolute;left:61px;top:-41px;width:79px;height:79px;border-radius:50%;background:var(--green);border:3px solid var(--white);display:flex;align-items:center;justify-content:center}
.card h3{margin-top:66px;font-size:14.5px;font-weight:500}
.card p{margin:18px 14px 0;font-size:10.5px;font-weight:700;line-height:17px}
.hours{margin:18px 0 0 22px;font-size:10.5px;font-weight:700;line-height:19px;text-align:left}
.hours td:first-child{width:65px}

/* difference */
.team-photo{left:87px;top:850px;width:441px;height:430px;background:linear-gradient(180deg,#f3f5f7 0%,#e3e8ed 60%,#d3dbe3 100%)}
.diff-title{left:592px;top:903px;font-size:19px;font-weight:400;letter-spacing:.3px}
.diff-text{left:593px;top:944px;font-size:10.8px;line-height:16.8px;white-space:nowrap}
.pill{height:55px;border-radius:0 28px 28px 0;color:var(--white);font-size:13px;font-weight:700;display:flex;align-items:center;padding-left:14px}

/* testimonials */
.testimonials{left:0;top:1280px;width:1200px;height:339px;background:radial-gradient(ellipse at 70% 40%,#1c3a4c 0%,#0f2433 50%,#07131c 100%)}
.t-title{left:0;top:1331px;width:1200px;text-align:center;color:var(--white);font-size:19px;font-weight:400}
.t-quote{left:300px;top:1393px;width:600px;text-align:center;color:var(--white);font-size:10.8px;font-weight:500;line-height:16.8px;white-space:nowrap}

/* blog */
.blog{left:0;top:1619px;width:1200px;height:405px;background:var(--paper)}
.blog-title{left:0;top:1680px;width:1200px;text-align:center;font-size:19px;font-weight:400}
.post-photo{top:1758px;width:192px;height:195px;background:linear-gradient(160deg,#e8ecef,#c9cfd5)}
.post{top:1758px;width:249px;height:200px;background:var(--white);box-shadow:4px 4px 0 #d6d6d6;padding:14px 16px}
.post h4{color:var(--blue-soft);font-size:13.5px;font-weight:500;line-height:17px}
.post .meta{margin-top:7px;font-size:9px}
.post .meta b{color:var(--green);font-weight:500}
.post p{margin-top:7px;font-size:9.5px;line-height:16px}
.likes{margin-top:12px;display:flex;align-items:center;gap:10px;font-size:13px}

/* footer */
.footer{left:0;top:2024px;width:1200px;height:287px;background:var(--footer)}
.f-brand{left:186px;top:2106px;color:var(--green);font-size:28px;font-weight:700;line-height:28px}
.f-brand small{display:block;color:var(--blue-soft);font-size:10px;font-weight:400;letter-spacing:1px;line-height:16px}
.f-social-label{left:187px;top:2178px;color:var(--blue-soft);font-size:12.5px}
.social{top:2206px;width:30px;height:30px;border:1.5px solid var(--white);border-radius:50%;display:flex;align-items:center;justify-content:center}
.f-head{color:var(--blue-soft);font-size:13.5px;font-weight:500}
.f-line{color:var(--white);font-size:13px}
.f-line b{color:var(--green-bright);font-weight:500}
.f-sub-text{left:820px;top:2134px;color:var(--white);font-size:10px;font-weight:500;line-height:12px;white-space:nowrap}
.f-input{left:821px;top:2189px;width:291px;height:43px;background:#2e3236;border-radius:0 22px 22px 0;color:var(--white);font-size:13px;padding-left:31px;display:flex;align-items:center}
.f-send{right:0;top:0;width:56px;height:43px;border-radius:22px;background:var(--green);display:flex;align-items:center;justify-content:center}
.copyright{left:0;top:2311px;width:1200px;height:51px;background:var(--green);color:var(--white);font-size:12px;font-weight:700;display:flex;align-items:center;justify-content:center}
</style>
</head>
<body>

<header class="topbar">
  <div class="abs phone-badge">
    <svg width="20" height="20" viewBox="0 0 24 24"><path fill="#fff" d="M6.6 10.8a15 15 0 0 0 6.6 6.6l2.2-2.2c.3-.3.7-.4 1-.2 1.1.4 2.3.6 3.6.6.6 0 1 .4 1 1V20c0 .6-.4 1-1 1A17 17 0 0 1 3 4c0-.6.4-1 1-1h3.5c.6 0 1 .4 1 1 0 1.3.2 2.5.6 3.6.1.3 0 .7-.2 1z"/></svg>
  </div>
  <div class="abs phone-line">Call on :555-0142</div>
  <div class="abs brand">FERNVALE<small>MEDICAL CLINIC</small></div>
  <div class="abs btn-book">BOOK AN APPOINTMENT</div>
</header>

<nav class="abs main-nav">
  <a class="active" style="left:78px">HOME</a>
  <a style="left:191px">ABOUT US</a>
  <a style="left:342px">WHAT TO EXPECT</a>
  <a style="left:485px">SERVICE</a>
  <a style="left:621px">TESTIMONIALS</a>
  <a style="left:749px">BLOG</a>
</nav>

<section class="abs hero">
  <div class="abs hero-photo" role="img" aria-label="Smiling female doctor with stethoscope in a bright clinic office"></div>
</section>
<h1 class="abs hero-title">WELCOME TO FERNVALE MEDICAL CLINIC</h1>
<p class="abs hero-text">Patient Access is a 24 hour online service whenever you need it, day or night.<br>Lorem Ipsum is simply dummy text of the printing and typesetting industry. Lorem<br>Ipsum has been the industry's standard dummy text ever since the 1500s, when an</p>
<div class="abs hero-btn">BOOK AN APPOINTMENT</div>
<div class="abs dots" style="left:88px;top:498px"><span></span><span></span><span class="on"></span><span></span><span></span></div>

<div class="abs card deep" style="left:173px">
  <div class="card-icon"><svg width="30" height="30" viewBox="0 0 24 24" fill="none" stroke="#fff" stroke-width="1.8"><rect x="3" y="5" width="15" height="14" rx="1"/><path d="M3 9h15M7 3v4M14 3v4"/><circle cx="18" cy="17" r="4" fill="#9bcb3c"/><path d="M18 15v2l1 1"/></svg></div>
  <h3>OPENING HOURS</h3>
  <table class="hours">
    <tr><td>Mon - Fri</td><td>8:00am to 9:00pm</td></tr>
    <tr><td>Saturday</td><td>8:00am to 5:00pm</td></tr>
    <tr><td>Sunday</td><td>8:00am to 3:00pm</td></tr>
  </table>
</div>
<div class="abs card soft" style="left:391px">
  <div class="card-icon"><svg width="30" height="30" viewBox="0 0 24 24"><path fill="#fff" d="M6.6 10.8a15 15 0 0 0 6.6 6.6l2.2-2.2c.3-.3.7-.4 1-.2 1.1.4 2.3.6 3.6.6.6 0 1 .4 1 1V20c0 .6-.4 1-1 1A17 17 0 0 1 3 4c0-.6.4-1 1-1h3.5c.6 0 1 .4 1 1 0 1.3.2 2.5.6 3.6.1.3 0 .7-.2 1z"/></svg></div>
  <h3>APPONTMENTS</h3>
  <p>The first step towards a healthy life is to schedule an appointment. Please contact our office by phon e or complete the appointment request form.</p>
</div>
<div class="abs card deep" style="left:606px">
  <div class="card-icon"><svg width="30" height="30" viewBox="0 0 24 24" fill="none" stroke="#fff" stroke-width="1.8"><rect x="4" y="5" width="16" height="15" rx="1"/><path d="M4 10h16M8 3v4M16 3v4"/></svg></div>
  <h3>DOCTORS TIMETABLE</h3>
  <p>The following is for guidance only to help you plan your appointment with a preferred doctor or nurse. It does not guarantee availability as the doctors or nurses may sometimes be attending to other duties.</p>
</div>
<div class="abs card soft" style="left:822px">
  <div class="card-icon"><svg width="30" height="30" viewBox="0 0 24 24"><rect x="3" y="7" width="18" height="13" rx="2" fill="#fff"/><path d="M9 7V5h6v2" stroke="#fff" stroke-width="2" fill="none"/><path d="M12 10v7M8.5 13.5h7" stroke="#9bcb3c" stroke-width="2.4"/></svg></div>
  <h3>EMERGENCY</h3>
  <p>Call us on : 555-0142</p>
</div>

<div class="abs team-photo" role="img" aria-label="Male doctor holding a clipboard beside a female doctor with stethoscope"></div>
<h2 class="abs diff-title">WHAT MAKES US DIFFERENT</h2>
<p class="abs diff-text">Lorem Ipsum is simply dummy text of the printing and typesetting industry. Lorem Ipsum has been the<br>industry'sstandard dummy text ever since the 1500s, when an unknown printer took a galley of type and<br>scrambled it to make a type specimen book. It has survived not only five centuries, but also<br>the leap into electronic typesetting, remaining essentially<br>unchanged. It was popularised in the 1960s with the release of Letraset sheets containing Lorem<br>Ipsum passages, and more recently with deskto</p>
<div class="abs pill" style="left:591px;top:1066px;width:231px;background:var(--blue-deep)">Modern Medicines</div>
<div class="abs pill" style="left:594px;top:1140px;width:290px;background:var(--blue-soft);padding-left:16px">Ambulance Services</div>
<div class="abs pill" style="left:592px;top:1211px;width:372px;background:var(--blue-soft)">Qualified Doctors and Staff</div>

<section class="abs testimonials"></section>
<h2 class="abs t-title">CLIENT TESTIMONIALS</h2>
<svg class="abs" style="left:320px;top:1362px" width="36" height="26" viewBox="0 0 36 26"><path fill="#9bcb3c" d="M0 10C0 3 5 0 10 0v5c-3 0-5 2-5 5h5v16H0zM19 10c0-7 5-10 10-10v5c-3 0-5 2-5 5h5v16H19z"/></svg>
<p class="abs t-quote">Lorem Ipsum is simply dummy text of the printing and typesetting industry. Lorem Ipsum has been the<br>industry'sstandard dummy text ever since the 1500s, when an unknown printer took a galley of type and<br>scrambled it to make a type specimen book. It has survived not only five centuries, but also<br>the leap into electronic typesetting, remaining essentially<br>unchanged. It was popularised in the 1960s with the release of Letraset sheets containing Lorem<br>Ipsum passages, and more recently with deskto</p>
<svg class="abs" style="left:733px;top:1480px" width="36" height="26" viewBox="0 0 36 26"><path fill="#9bcb3c" d="M36 16c0 7-5 10-10 10v-5c3 0 5-2 5-5h-5V0h10zM17 16c0 7-5 10-10 10v-5c3 0 5-2 5-5H7V0h10z"/></svg>
<div class="abs dots" style="left:558px;top:1585px"><span style="background:#6f8a93"></span><span style="background:#6f8a93"></span><span class="on"></span><span style="background:#6f8a93"></span><span style="background:#6f8a93"></span></div>

<section class="abs blog"></section>
<h2 class="abs blog-title">BLOG POST</h2>
<div class="abs post-photo" style="left:131px" role="img" aria-label="Doctor consulting with a worried patient"></div>
<article class="abs post" style="left:332px">
  <h4>Lorem Ipsum is simply dummy text of the printing and typesetting</h4>
  <div class="meta">June 21, 2016 at 8:12pm &nbsp;|&nbsp; <b>Healthy Lifestyle</b></div>
  <p>Lorem Ipsum is simply dummy text of the printing and typesetting industry. Lorem Ipsum has been the industry's standard dummy text ever since the 1500s, when an unknown printer took a galley of</p>
  <div class="likes"><svg width="16" height="15" viewBox="0 0 24 22"><path fill="#9bcb3c" d="M0 9h5v13H0zM7 21V9l6-9c2 0 3 1 3 3l-1 5h7c1 0 2 1 2 2l-3 10c0 1-1 1-2 1z"/></svg>3</div>
</article>
<div class="abs post-photo" style="left:617px" role="img" aria-label="Portrait of a smiling female doctor"></div>
<article class="abs post" style="left:819px">
  <h4>Lorem Ipsum is simply dummy text of the printing and typesetting</h4>
  <div class="meta">June 21, 2016 at 8:12pm &nbsp;|&nbsp; <b>Healthy Lifestyle</b></div>
  <p>Lorem Ipsum is simply dummy text of the printing and typesetting industry. Lorem Ipsum has been the industry's standard dummy text ever since the 1500s, when an unknown printer took a galley of</p>
  <div class="likes"><svg width="16" height="15" viewBox="0 0 24 22"><path fill="#9bcb3c" d="M0 9h5v13H0zM7 21V9l6-9c2 0 3 1 3 3l-1 5h7c1 0 2 1 2 2l-3 10c0 1-1 1-2 1z"/></svg>21</div>
</article>

<footer class="abs footer"></footer>
<div class="abs f-brand">FERNVALE<small>MEDICAL &nbsp;CLINIC</small></div>
<div class="abs f-social-label">Connected with social media</div>
<div class="abs social" style="left:190px" aria-label="Social profile link">
  <svg width="15" height="15" viewBox="0 0 24 24" fill="none" stroke="#fff" stroke-width="2.2" stroke-linecap="round"><path d="M10 14a4 4 0 0 0 6 0l3-3a4 4 0 0 0-6-6l-1 1"/><path d="M14 10a4 4 0 0 0-6 0l-3 3a4 4 0 0 0 6 6l1-1"/></svg>
</div>
<div class="abs social" style="left:232px" aria-label="Social profile chat">
  <svg width="15" height="15" viewBox="0 0 24 24" fill="none" stroke="#fff" stroke-width="2.2" stroke-linejoin="round"><path d="M4 5h16v11H10l-5 4v-4H4z"/></svg>
</div>
<div class="abs social" style="left:273px" aria-label="Social profile share">
  <svg width="15" height="15" viewBox="0 0 24 24" fill="#fff" stroke="#fff" stroke-width="2"><circle cx="18" cy="5" r="2.5"/><circle cx="6" cy="12" r="2.5"/><circle cx="18" cy="19" r="2.5"/><path d="M8 11l8-5M8 13l8 5" fill="none"/></svg>
</div>

<div class="abs f-head" style="left:428px;top:2110px">CONTACT US</div>
<div class="abs f-line" style="left:428px;top:2145px"><b>CALL ON :</b> 555-0187</div>
<div class="abs f-line" style="left:430px;top:2178px;width:360px;line-height:18px"><b>LOCATION :</b> Lorem Ipsum is simply dummy t<br><span style="padding-left:83px">ext of the printing and typesetting industry.</span></div>
<div class="abs f-line" style="left:430px;top:2224px"><b>EMAIL US :</b> hello@fernvaleclinic.example</div>

<div class="abs f-head" style="left:820px;top:2107px">SUBSCRIBE FOR OUR NEWS LETTER</div>
<p class="abs f-sub-text">Enter your email address to receive up-to-date news,<br>new patient information and other useful stuff, delivered<br>right to your inbox.</p>
<div class="abs f-input">Your message
  <div class="abs f-send"><svg width="26" height="18" viewBox="0 0 26 18" fill="none" stroke="#fff" stroke-width="1.6"><rect x="1" y="1" width="24" height="16"/><path d="M1 1l12 9 12-9"/></svg></div>
</div>
<div class="abs copyright">Copyright © 2017 Fernvale medical clinic</div>

</body>
</html>
```